Business Card cabinets and cabinets components making company.

the card should be formal and interesting at the same time. The main colors will be black and white.

Font styles to use
Sans Serif

Colors

Designer to choose only greyscale colors for use in the design.

Requirements
Must have
• At least must have the followings:
office phone
cell phone
address
position
name
email
web

```html
<!DOCTYPE html>
<html lang="en">
<head>
<meta charset="utf-8">
<title>Panelwright Business Card</title>
<link href="https://fonts.googleapis.com/css2?family=Montserrat:wght@400;700&display=swap" rel="stylesheet">
<style>
  :root {
    --backdrop: #262626;
    --card: #141414;
    --card-shade: #1b1b1b;
    --ink: #ffffff;
    --rule: #bdbdbd;
  }
  * { margin: 0; padding: 0; box-sizing: border-box; }
  html, body {
    width: 1200px; height: 852px; overflow: hidden;
    background: var(--backdrop);
    font-family: "Montserrat", sans-serif;
    color: var(--ink);
  }
  .stage {
    position: relative; width: 1200px; height: 852px;
    display: flex; flex-direction: column; align-items: center;
    justify-content: center; gap: 56px;
  }
  .card {
    position: relative; width: 525px; height: 300px;
    background: var(--card); border-radius: 16px; overflow: hidden;
    box-shadow: 0 10px 24px rgba(0,0,0,.45);
  }
  .brand {
    font-weight: 700; color: var(--ink); letter-spacing: .5px;
    display: flex; align-items: center; gap: 10px;
  }
  .brand-mark { width: 14px; height: 14px; background: var(--ink); }

  /* front */
  .card--front .cabinet-art {
    position: absolute; right: 0; top: 0; width: 230px; height: 100%;
    background: linear-gradient(160deg, var(--card-shade), var(--card));
  }
  .card--front .brand {
    position: absolute; left: 50%; top: 50%;
    transform: translate(-50%, -50%); font-size: 44px;
  }
  .card--front .brand-mark { width: 22px; height: 22px; }

  /* back */
  .card--back .divider { position: absolute; inset: 0; }
  .card--back .brand {
    position: absolute; right: 44px; top: 40px; font-size: 28px; line-height: 1;
  }
  .person { position: absolute; left: 34px; top: 122px; }
  .person-name { font-weight: 700; font-size: 17px; letter-spacing: 1.5px; text-transform: uppercase; }
  .person-role { font-size: 12px; margin-top: 3px; }
  .address {
    position: absolute; right: 34px; top: 136px;
    text-align: right; font-size: 11.5px; line-height: 1.45; font-style: normal;
  }
  .contacts {
    position: absolute; left: 46px; bottom: 22px;
    list-style: none; font-size: 11.5px; line-height: 1.55;
  }
  .contacts li { display: flex; align-items: center; gap: 7px; }
  .contacts svg { width: 10px; height: 10px; fill: var(--ink); flex: none; }
</style>
</head>
<body>
<main class="stage">
  <section class="card card--front">
    <div class="cabinet-art" role="img" aria-label="Faint cabinet illustration in dark grey"></div>
    <div class="brand"><span class="brand-mark"></span>Panelwright</div>
  </section>

  <section class="card card--back">
    <svg class="divider" viewBox="0 0 525 300" aria-hidden="true">
      <line x1="46" y1="198" x2="470" y2="86" stroke="var(--rule)" stroke-width="0.8"/>
    </svg>
    <div class="brand"><span class="brand-mark"></span>Panelwright</div>
    <div class="person">
      <p class="person-name">Daniel Reyes</p>
      <p class="person-role">Owner/CEO</p>
    </div>
    <address class="address">
      418 Birch Hollow Road<br>Marlow County district 7420
    </address>
    <ul class="contacts">
      <li><svg viewBox="0 0 10 10"><path d="M2 0.5 3.6 2.6 2.6 3.6Q3.6 5.8 6.4 7.4L7.4 6.4 9.5 8 8.4 9.5Q4.5 9 1.5 5.5 0.5 3 2 0.5Z"/></svg>555-210-4837</li>
      <li><svg viewBox="0 0 10 10"><path d="M2.5 0h5v10h-5zM3.3 1v7h3.4V1z"/></svg>5550 987 654</li>
      <li><svg viewBox="0 0 10 10"><path d="M0 2h10v6H0zM1 3v.3l4 2.5 4-2.5V3z"/></svg>info@panelwright.com</li>
      <li><svg viewBox="0 0 10 10"><circle cx="5" cy="5" r="4.5"/></svg>www.panelwright.com</li>
    </ul>
  </section>
</main>
</body>
</html>
```